Simple elegant feminine design - Going out on my own as a Mortgage Broker.
My thoughts are the following details on the Front, middle of the card possibly? Phone and email smaller font than my name?
Marnie Veltrin
Finance Specialist
p: 0438 215 962
e: marnie@veltrinlending.com.au
Bottom of the card
residential / commercial / equipment
I would like the Font in Rose Gold maybe white or black background? or Possibly a stone grey - are you able to do a few options? I'd like them embossed
Then I had an idea as a simple logo as per the attached if you get the idea in my scribble, my initials, capital M attached to a small v that leads/follows into a circle? Thicker Font In Rose Gold, middle of the card at the back.
Very open to ideas though and what colour you think would look better with the Rose Gold.
Thanks so much for your help, I am not very creative and savvy with this stuff :-)
Industry/Entity Type
Finance
Contact Information for Business Card
Marnie Veltrin
p: 0438 215 962
Look and feel

```html
<!DOCTYPE html>
<html lang="en">
<head>
<meta charset="utf-8">
<title>Marnie Veltrin – Business Cards</title>
<link rel="stylesheet" href="https://fonts.googleapis.com/css2?family=Montserrat:wght@300;400;600;700&display=swap">
<style>
  :root {
    --stage: #5c6366;
    --rose: #c9968a;
    --rose-light: #e3b9ab;
    --ink: #1b1a1a;
    --stone: #8f8a86;
    --photo-light: #dcd6d3;
    --photo-dark: #7f7a78;
    --muted: #d2c6c1;
  }
  html, body {
    margin: 0;
    padding: 0;
    width: 1200px;
    height: 906px;
    overflow: hidden;
    background: var(--stage);
    font-family: "Montserrat", sans-serif;
  }
  .canvas {
    position: relative;
    width: 1200px;
    height: 906px;
  }
  .card {
    position: absolute;
    top: 293px;
    width: 540px;
    height: 320px;
    box-shadow: 0 18px 40px rgba(0,0,0,0.35);
    overflow: hidden;
  }
  .card--front { left: 40px; }
  .card--back { left: 620px; background: var(--rose); }
  .card svg { position: absolute; inset: 0; display: block; }

  .brand {
    position: absolute;
    display: flex;
    align-items: center;
    gap: 8px;
    color: var(--ink);
    font-weight: 700;
    text-transform: uppercase;
  }
  .brand__ring {
    border: 4px solid var(--ink);
    border-radius: 50%;
    box-sizing: border-box;
  }
  .card--front .brand {
    left: 0;
    width: 148px;
    top: 146px;
    flex-direction: column;
    font-size: 11px;
    letter-spacing: 2px;
  }
  .card--front .brand__ring { width: 54px; height: 54px; }

  .identity {
    position: absolute;
    left: 172px;
    top: 156px;
    color: var(--rose);
    text-transform: uppercase;
  }
  .identity__name {
    margin: 0;
    font-size: 20px;
    line-height: 1;
    letter-spacing: 0.5px;
  }
  .identity__first { font-weight: 700; }
  .identity__last { font-weight: 300; color: var(--rose-light); }
  .identity__role {
    margin: 5px 0 0;
    font-size: 10px;
    font-weight: 600;
    letter-spacing: 0.8px;
  }
  .contact {
    list-style: none;
    margin: 20px 0 0;
    padding: 0;
    text-transform: none;
    color: var(--muted);
    font-size: 9px;
    font-weight: 400;
  }
  .contact li {
    display: flex;
    align-items: center;
    gap: 10px;
    margin-bottom: 9px;
  }
  .contact svg { position: static; width: 11px; height: 11px; }

  .services {
    position: absolute;
    left: 172px;
    top: 288px;
    margin: 0;
    color: var(--rose);
    font-size: 8px;
    font-weight: 600;
    letter-spacing: 1.6px;
    text-transform: uppercase;
    white-space: nowrap;
  }

  .card--back .brand {
    left: 50%;
    top: 50%;
    transform: translate(-50%, -50%);
    gap: 12px;
    font-size: 26px;
    font-weight: 600;
    letter-spacing: 0.5px;
    white-space: nowrap;
  }
  .card--back .brand__ring { width: 50px; height: 50px; }
</style>
</head>
<body>
<main class="canvas">

  <section class="card card--front" aria-label="Business card front">
    <svg viewBox="0 0 540 320" width="540" height="320" aria-hidden="true">
      <defs>
        <linearGradient id="skyline-tone" x1="0" y1="0" x2="1" y2="1">
          <stop offset="0" stop-color="var(--photo-light)"/>
          <stop offset="1" stop-color="var(--photo-dark)"/>
        </linearGradient>
      </defs>
      <rect class="card__base" width="540" height="320" fill="var(--rose)"/>
      <polygon class="card__panel" points="148,100 290,100 325,128 518,128 518,250 494,274 494,320 148,320" fill="var(--ink)"/>
    </svg>
    <svg viewBox="0 0 540 320" width="540" height="320" role="img" aria-label="Black and white photograph of a city skyline with tall office towers">
      <polygon class="card__photo" points="148,0 540,0 540,128 325,128 290,100 148,100" fill="url(#skyline-tone)"/>
    </svg>

    <div class="brand">
      <span class="brand__ring"></span>
      <span class="brand__name">Veltrin</span>
    </div>

    <div class="identity">
      <h1 class="identity__name"><span class="identity__first">Marnie</span> <span class="identity__last">Veltrin</span></h1>
      <p class="identity__role">Finance Specialist</p>
      <ul class="contact">
        <li>
          <svg viewBox="0 0 12 12" aria-hidden="true"><path d="M3 1.5 L4.6 3.6 L3.8 4.6 Q5 7 7.4 8.2 L8.4 7.4 L10.5 9 L9.6 10.5 Q5.5 10.5 1.5 2.4 Z" fill="none" stroke="var(--muted)" stroke-width="0.9"/></svg>
          <span>0438 215 962</span>
        </li>
        <li>
          <svg viewBox="0 0 12 12" aria-hidden="true"><rect x="1" y="2.5" width="10" height="7" fill="none" stroke="var(--muted)" stroke-width="0.9"/><path d="M1 2.5 L6 6.5 L11 2.5" fill="none" stroke="var(--muted)" stroke-width="0.9"/></svg>
          <span>marnie@veltrinlending.com.au</span>
        </li>
      </ul>
    </div>

    <p class="services">Residential / Commercial / Equipment</p>
  </section>

  <section class="card card--back" aria-label="Business card back">
    <div class="brand">
      <span class="brand__ring"></span>
      <span class="brand__name">Marnie Veltrin</span>
    </div>
  </section>

</main>
</body>
</html>
```